Business card design for global fintech startup

Veltrix is a modern payments platform for the global insurance industry, serving international health, life, and travel insurers, MGAs, brokers, and partners.

We need a professional, premium business card for use at insurance conferences and executive meetings. The goal is to create a card that feels trustworthy, modern, and high-quality, while still being distinctive and memorable in a stack of business cards.

Target audience:
Senior insurance executives (VP, C-suite).

Design goals:
Clear, professional, and credible
Modern but not trendy
Premium and well-structured
Easy to read and practical for networking

Brand direction:
Brand-first (company over individual)
Follow existing brand guidelines where possible
Clean layout, strong hierarchy, excellent readability

Must include:
Name
Title
Company name (Veltrix)
Logo
Email
Phone/Whatsapp
Website (www.withveltrix.example)
Tagline - Clarity in every payment

Materials & finish:
Open to designer recommendations for premium look and feel.

Please avoid:
Flashy or trendy startup styles
Generic insurance icons or clichés
Cluttered layouts or hard-to-read text

Deliverables:
Front and back business card, print-ready files.

Target Market(s)

Global Insurance executives

Industry/Entity Type

Fintech, Insurtech, Insurance, Financial Services

Contact Information for Business Card

Name Title Company name (Veltrix) Logo Email Phone/Whatsapp Website (www.withveltrix.example) Tagline - Clarity in every payment

Font styles to use
Other font styles liked:
• See brand guidelines

Requirements
Nice to have
• something that stands out/makes us more memorable while still remaining professional
Should not have
• Please avoid: Flashy or trendy startup styles Generic insurance icons or clichés Cluttered layouts or hard-to-read text

```html
<!DOCTYPE html>
<html lang="en">
<head>
<meta charset="utf-8">
<title>Veltrix Business Card – Front and Back</title>
<link rel="stylesheet" href="https://fonts.googleapis.com/css2?family=Montserrat:wght@500;600&family=Nunito:wght@600&display=swap">
<style>
  :root {
    --canvas: #d9dadc;
    --card-white: #ffffff;
    --card-black: #1d1d1e;
    --ink: #1b1b1b;
    --ink-soft: #2a2a2a;
    --sky: #4fc3ea;
    --blue: #3d8fd6;
    --purple: #6a3f9b;
    --orange: #ec7312;
    --yellow: #f8c54c;
    --divider: #9a9a9a;
  }
  * { box-sizing: border-box; margin: 0; padding: 0; }
  html, body { width: 1200px; height: 1200px; overflow: hidden; }
  body {
    background: var(--canvas);
    font-family: "Montserrat", Arial, sans-serif;
    color: var(--ink);
    position: relative;
  }
  .card {
    position: absolute;
    left: 150px;
    width: 900px;
    height: 514px;
    border-radius: 36px;
    overflow: hidden;
  }
  .card--front { top: 60px; background: var(--card-white); }
  .card--back {
    top: 626px;
    background: var(--card-black);
    box-shadow: inset 0 -4px 0 var(--sky);
  }

  /* front */
  .brand {
    position: absolute;
    left: 150px;
    top: 112px;
    display: flex;
    align-items: center;
    gap: 22px;
  }
  .brand__dot {
    width: 54px; height: 54px; border-radius: 50%;
    background: var(--blue);
  }
  .brand__name {
    font-family: "Montserrat", Arial, sans-serif;
    font-weight: 600;
    font-size: 66px;
    letter-spacing: 7px;
    color: var(--ink);
    text-transform: uppercase;
    line-height: 1;
  }
  .tagline {
    position: absolute;
    left: 226px;
    top: 200px;
    font-family: "Nunito", Arial, sans-serif;
    font-weight: 600;
    font-size: 28px;
    letter-spacing: 1.5px;
    color: var(--ink-soft);
  }
  .divider {
    position: absolute;
    left: 450px;
    top: 290px;
    width: 1px;
    height: 120px;
    background: var(--divider);
  }
  .person {
    position: absolute;
    left: 90px;
    top: 330px;
  }
  .person__name {
    font-family: "Montserrat", Arial, sans-serif;
    font-weight: 600;
    font-size: 46px;
    color: var(--sky);
    text-transform: uppercase;
    line-height: 1;
  }
  .person__title {
    font-family: "Montserrat", Arial, sans-serif;
    font-weight: 500;
    font-size: 27px;
    color: var(--ink);
    text-transform: uppercase;
    margin-top: 6px;
    margin-left: 30px;
  }
  .contact {
    position: absolute;
    left: 500px;
    top: 268px;
    list-style: none;
    font-family: "Nunito", Arial, sans-serif;
    font-weight: 600;
    font-size: 25px;
    color: var(--ink);
  }
  .contact__item {
    display: flex;
    align-items: center;
    gap: 12px;
    height: 44px;
  }
  .contact__icon { width: 28px; height: 28px; flex: none; }
  .contact__item--phone { font-size: 30px; letter-spacing: 1px; }

  .color-band {
    position: absolute;
    left: 0; right: 0; bottom: 0;
    height: 16px;
    display: flex;
  }
  .color-band span { height: 100%; }
  .color-band .sky { flex: 26; background: var(--sky); }
  .color-band .blue { flex: 22; background: var(--blue); }
  .color-band .purple { flex: 20; background: var(--purple); }
  .color-band .orange { flex: 20; background: var(--orange); }
  .color-band .yellow { flex: 12; background: var(--yellow); }

  /* back */
  .back__texture {
    position: absolute; inset: 0;
    background: radial-gradient(ellipse at 50% 45%, #262627 0%, var(--card-black) 70%);
  }
  .brand--back {
    left: 0; right: 0; top: 0; bottom: 0;
    justify-content: center;
    padding-left: 120px;
  }
  .brand--back .brand__name { color: #ffffff; font-size: 70px; }
</style>
</head>
<body>

  <section class="card card--front" aria-label="Business card front">
    <div class="brand">
      <span class="brand__dot"></span>
      <span class="brand__name">Veltrix</span>
    </div>
    <p class="tagline">Clarity in every payment</p>

    <div class="person">
      <p class="person__name">Full Name</p>
      <p class="person__title">Title</p>
    </div>

    <div class="divider"></div>

    <ul class="contact">
      <li class="contact__item contact__item--phone">
        <svg class="contact__icon" viewBox="0 0 28 28" aria-hidden="true">
          <circle cx="14" cy="14" r="11.5" fill="none" stroke="var(--sky)" stroke-width="2.5"/>
          <path d="M10 8.5c-1 .8-1.5 2 0 4.5s3.5 4.5 5.5 5.5 3 .3 3.8-.8l-2.3-1.8-1.3.9c-1.3-.6-2.7-2-3.4-3.3l.8-1.4-1.6-2.4z" fill="var(--sky)"/>
        </svg>
        <span>(000) 000 0000</span>
      </li>
      <li class="contact__item">
        <svg class="contact__icon" viewBox="0 0 28 28" aria-hidden="true">
          <rect x="2" y="6" width="24" height="16" rx="1.5" fill="var(--sky)"/>
          <path d="M2.5 7L14 16 25.5 7" fill="none" stroke="#fff" stroke-width="2"/>
        </svg>
        <span>email@company.com</span>
      </li>
      <li class="contact__item">
        <svg class="contact__icon" viewBox="0 0 28 28" aria-hidden="true">
          <g fill="none" stroke="var(--sky)" stroke-width="2">
            <circle cx="14" cy="14" r="11"/>
            <ellipse cx="14" cy="14" rx="5" ry="11"/>
            <path d="M3 14h22M5 8h18M5 20h18"/>
          </g>
        </svg>
        <span>www.withveltrix.example</span>
      </li>
    </ul>

    <div class="color-band" aria-hidden="true">
      <span class="sky"></span><span class="blue"></span><span class="purple"></span><span class="orange"></span><span class="yellow"></span>
    </div>
  </section>

  <section class="card card--back" aria-label="Business card back">
    <div class="back__texture" role="img" aria-label="Subtle repeating embossed brand pattern on black stock"></div>
    <div class="brand brand--back">
      <span class="brand__dot"></span>
      <span class="brand__name">Veltrix</span>
    </div>
  </section>

</body>
</html>
```